Haldor Snekker AS
Buiness cards for haldor snekker as
Haldor Snekker AS - Construction
Creative Brief
Simple
Tobias Kranveldt
CEO
Lerkeskogveien 14 0587 OSLO Norway
post@haldorsnekker.example
www.haldorsnekker.example
Org. nr.: 836 402 517
Its for a company that expanse fast within big building sites
come up with something!?! we make your investment possible

```html
<!DOCTYPE html>
<html lang="en">
<head>
<meta charset="utf-8">
<title>Haldor Snekker AS – Business Cards</title>
<link rel="stylesheet" href="https://fonts.googleapis.com/css2?family=Open+Sans:wght@400;600;700&display=swap">
<style>
  :root {
    --stage: #3b3b3d;
    --card-white: #fbfbfb;
    --brand-blue: #2b4b73;
    --brand-blue-dark: #223c5e;
    --name-blue: #2f5a8c;
    --text-grey: #555a60;
    --tagline: #a9c2df;
    --logo-grey: #5a6068;
  }
  * { margin: 0; padding: 0; box-sizing: border-box; }
  html, body { width: 1200px; height: 751px; overflow: hidden; }
  body {
    background: var(--stage);
    font-family: "Open Sans", Arial, sans-serif;
    position: relative;
  }
  .card {
    position: absolute;
    top: 221px;
    width: 492px;
    height: 278px;
    box-shadow: 0 6px 18px rgba(0,0,0,.45);
  }
  .card--front { left: 91px; background: var(--card-white); }
  .card--back { left: 619px; background: var(--brand-blue); }

  .wordmark {
    position: absolute;
    left: 0; right: 0;
    display: flex;
    flex-direction: column;
    align-items: center;
    gap: 8px;
  }
  .wordmark__square {
    width: 64px; height: 44px;
    border-radius: 2px;
  }
  .wordmark__name {
    font-weight: 700;
    font-size: 20px;
    letter-spacing: .5px;
    text-transform: uppercase;
  }
  .card--front .wordmark { top: 26px; }
  .card--front .wordmark__square { background: var(--brand-blue); }
  .card--front .wordmark__name { color: var(--logo-grey); }
  .card--back .wordmark { top: 96px; }
  .card--back .wordmark__square { background: #e9edf2; }
  .card--back .wordmark__name { color: #ffffff; }

  .accent {
    position: absolute;
    top: 172px;
    width: 8px;
    height: 68px;
    background: var(--brand-blue);
  }
  .accent--left { left: 0; }
  .accent--right { right: 0; }

  .person {
    position: absolute;
    left: 28px;
    top: 178px;
    color: var(--text-grey);
    font-size: 11px;
    line-height: 19px;
  }
  .person__name {
    color: var(--name-blue);
    font-weight: 600;
    font-size: 17px;
    line-height: 24px;
  }

  .contacts {
    position: absolute;
    right: 24px;
    top: 182px;
    list-style: none;
    font-size: 11px;
    line-height: 19px;
    color: var(--text-grey);
    text-align: right;
  }
  .contacts li { display: flex; align-items: center; justify-content: flex-end; gap: 8px; }
  .contacts svg { width: 11px; height: 11px; fill: var(--brand-blue); flex: none; }

  .tagline {
    position: absolute;
    left: 134px;
    top: 212px;
    font-size: 12px;
    color: var(--tagline);
  }
</style>
</head>
<body>
  <section class="card card--front" aria-label="Business card front">
    <div class="wordmark">
      <div class="wordmark__square"></div>
      <div class="wordmark__name">Haldor Snekker AS</div>
    </div>
    <span class="accent accent--left"></span>
    <span class="accent accent--right"></span>

    <div class="person">
      <p class="person__name">Tobias Kranveldt</p>
      <p>CEO</p>
      <p>Lerkeskogveien 14 0587 OSLO, Norway</p>
      <p>Lin : 836 402 517</p>
    </div>

    <ul class="contacts">
      <li>+47 9000 4812
        <svg viewBox="0 0 12 12"><rect x="3" y="0" width="6" height="12" rx="1"/><rect x="4" y="1.5" width="4" height="8" fill="#fbfbfb"/></svg></li>
      <li>+47 2100 5936
        <svg viewBox="0 0 12 12"><rect x="0" y="4" width="12" height="7" rx="1"/><rect x="3" y="0" width="6" height="5"/></svg></li>
      <li>post@haldorsnekker.example
        <svg viewBox="0 0 12 12"><rect x="0" y="2" width="12" height="8" rx="1"/><path d="M0.5 2.5 6 7 11.5 2.5" stroke="#fbfbfb" stroke-width="1.2" fill="none"/></svg></li>
      <li>www.haldorsnekker.example
        <svg viewBox="0 0 12 12"><circle cx="6" cy="6" r="6"/><circle cx="6" cy="6" r="3" fill="#fbfbfb"/></svg></li>
    </ul>
  </section>

  <section class="card card--back" aria-label="Business card back">
    <div class="wordmark">
      <div class="wordmark__square"></div>
      <div class="wordmark__name">Haldor Snekker AS</div>
    </div>
    <p class="tagline">we make your investment possible</p>
  </section>
</body>
</html>
```